Linking together of The Calm Grid, stride onward and foreguard.

Quiet your steps (The Calm Grid), stride onward, and Foreguard are 3 treatment programs for people with chronic pain.
Quiet your steps is 1st. Here I aim to half peoples pain, then halve it again and again until it is gone, or they no longer care about it.
Stride onward is a rehabilitation program. We get people to identify the things that their pain has taken from them, and then we take it back. (ie Take back what's yours')
Foreguard is a disease prevention program. It is targeted at identifying diseases of ageing and slowing their progression, or hopefully preventing their onset.
My wife has suggested we linked them together like cogs working together. As one cog turns all the others do, thus as we decrease pain, we start the wheels turning of taking back what you have lost.
I have attach some cogs pictures so you can see what I mean.
I was thinking that The Calm Grid could be like spokes on a bicycle wheel.
For Stride onward similar to The Calm Grid can you have 5 sections
1. Mindset
2. Workout
3. Diet
5. Recover
6. Socialise
For Foreguard, I am still developing its components. I will leave that to you.
Send me some questions if this doesn't make sense.
When I set this project up, I had set it up for a designer I have been working with. He completed 2 other jobs for me and hasn't got to this. Can it please be extended? Cheers Rob

```html
<!DOCTYPE html>
<html lang="en">
<head>
<meta charset="utf-8">
<title>3 Treatment Programs</title>
<link rel="stylesheet" href="https://fonts.googleapis.com/css2?family=Poppins:wght@300;500;700&display=swap">
<style>
  :root {
    --ink: #2b2b2b;
    --ink-soft: #3a3a3a;
    --paper: #ffffff;
    --link-grey: #e6e6e6;
    --calm-red: #f20c0c;
    --foreguard-teal: #13a595;
    --stride-blue: #1f6fc6;
    --stride-deep: #1d3aa6;
    --stride-light: #4d74ee;
  }
  html, body {
    margin: 0;
    padding: 0;
    width: 1200px;
    height: 1200px;
    overflow: hidden;
    background: var(--paper);
  }
  .canvas {
    position: relative;
    width: 1200px;
    height: 1200px;
    font-family: "Poppins", sans-serif;
  }
  .heading {
    position: absolute;
    left: 86px;
    top: 80px;
    margin: 0;
    color: var(--ink);
  }
  .heading__main {
    display: block;
    font-weight: 700;
    font-size: 42px;
    line-height: 1.15;
    letter-spacing: 0.5px;
  }
  .heading__sub {
    display: block;
    font-weight: 300;
    font-size: 36px;
    line-height: 1.3;
    letter-spacing: 0.3px;
    color: var(--ink-soft);
  }
  .cog-system {
    position: absolute;
    left: 0;
    top: 0;
    width: 1200px;
    height: 1200px;
  }
  .program-name {
    font-family: "Poppins", sans-serif;
    font-weight: 700;
    font-size: 36px;
    fill: var(--ink);
  }
  .pillar-label {
    font-family: "Poppins", sans-serif;
    font-weight: 500;
    font-size: 19px;
    fill: var(--paper);
  }
</style>
</head>
<body>
<main class="canvas">
  <h1 class="heading">
    <span class="heading__main">3 TREATMENT PROGRAMS</span>
    <span class="heading__sub">FOR PEOPLE WITH CHRONIC PAIN</span>
  </h1>

  <svg class="cog-system" viewBox="0 0 1200 1200" xmlns="http://www.w3.org/2000/svg" aria-label="Three linked cogs: The Calm Grid, Foreguard and Stride Onward">
    <defs>
      <radialGradient id="stride-fill" cx="35%" cy="30%" r="80%">
        <stop offset="0" stop-color="var(--stride-light)"/>
        <stop offset="1" stop-color="var(--stride-deep)"/>
      </radialGradient>

      <g id="cog-teeth">
        <rect x="-8" y="-161" width="16" height="24" transform="rotate(0)"/>
        <rect x="-8" y="-161" width="16" height="24" transform="rotate(15)"/>
        <rect x="-8" y="-161" width="16" height="24" transform="rotate(30)"/>
        <rect x="-8" y="-161" width="16" height="24" transform="rotate(45)"/>
        <rect x="-8" y="-161" width="16" height="24" transform="rotate(60)"/>
        <rect x="-8" y="-161" width="16" height="24" transform="rotate(75)"/>
        <rect x="-8" y="-161" width="16" height="24" transform="rotate(90)"/>
        <rect x="-8" y="-161" width="16" height="24" transform="rotate(105)"/>
        <rect x="-8" y="-161" width="16" height="24" transform="rotate(120)"/>
        <rect x="-8" y="-161" width="16" height="24" transform="rotate(135)"/>
        <rect x="-8" y="-161" width="16" height="24" transform="rotate(150)"/>
        <rect x="-8" y="-161" width="16" height="24" transform="rotate(165)"/>
        <rect x="-8" y="-161" width="16" height="24" transform="rotate(180)"/>
        <rect x="-8" y="-161" width="16" height="24" transform="rotate(195)"/>
        <rect x="-8" y="-161" width="16" height="24" transform="rotate(210)"/>
        <rect x="-8" y="-161" width="16" height="24" transform="rotate(225)"/>
        <rect x="-8" y="-161" width="16" height="24" transform="rotate(240)"/>
        <rect x="-8" y="-161" width="16" height="24" transform="rotate(255)"/>
        <rect x="-8" y="-161" width="16" height="24" transform="rotate(270)"/>
        <rect x="-8" y="-161" width="16" height="24" transform="rotate(285)"/>
        <rect x="-8" y="-161" width="16" height="24" transform="rotate(300)"/>
        <rect x="-8" y="-161" width="16" height="24" transform="rotate(315)"/>
        <rect x="-8" y="-161" width="16" height="24" transform="rotate(330)"/>
        <rect x="-8" y="-161" width="16" height="24" transform="rotate(345)"/>
        <circle r="145"/>
      </g>

      <g id="cog-spokes">
        <line x1="0" y1="0" x2="0" y2="-134"/>
        <line x1="0" y1="0" x2="0" y2="-134" transform="rotate(72)"/>
        <line x1="0" y1="0" x2="0" y2="-134" transform="rotate(144)"/>
        <line x1="0" y1="0" x2="0" y2="-134" transform="rotate(216)"/>
        <line x1="0" y1="0" x2="0" y2="-134" transform="rotate(288)"/>
      </g>

      <path id="calm-grid-arc" d="M434.6 446.8 A168 168 0 0 1 765.4 446.8"/>
      <path id="foreguard-arc" d="M313 623 A185 185 0 0 0 524.5 925"/>
      <path id="stride-arc" d="M677 912 A176 176 0 0 0 883.5 628"/>
    </defs>

    <!-- linking triangle -->
    <polygon class="link-frame" points="600,330 308,922 892,922" fill="none" stroke="var(--link-grey)" stroke-width="16" stroke-linejoin="round"/>

    <!-- The Calm Grid -->
    <g class="cog cog--calm-grid" transform="translate(600 476)">
      <use href="#cog-teeth" fill="var(--calm-red)"/>
      <circle r="130" fill="var(--paper)"/>
      <use href="#cog-spokes" stroke="var(--calm-red)" stroke-width="11"/>
      <circle r="33" fill="var(--calm-red)"/>
      <circle r="22" fill="var(--paper)"/>
    </g>

    <!-- Foreguard -->
    <g class="cog cog--foreguard" transform="translate(432 765)">
      <use href="#cog-teeth" fill="var(--foreguard-teal)"/>
      <circle r="130" fill="var(--paper)"/>
      <use href="#cog-spokes" stroke="var(--foreguard-teal)" stroke-width="11"/>
      <circle r="33" fill="var(--foreguard-teal)"/>
      <circle r="22" fill="var(--paper)"/>
    </g>

    <!-- Stride Onward -->
    <g class="cog cog--stride" transform="translate(768 761)">
      <use href="#cog-teeth" fill="var(--stride-blue)"/>
      <circle r="132" fill="url(#stride-fill)"/>
      <use href="#cog-spokes" stroke="var(--paper)" stroke-width="9"/>
      <circle r="33" fill="var(--stride-blue)"/>
      <circle r="21" fill="url(#stride-fill)"/>
      <text class="pillar-label" x="-54" y="-60" text-anchor="middle" dominant-baseline="middle">Socialise</text>
      <text class="pillar-label" x="54" y="-60" text-anchor="middle" dominant-baseline="middle">Mindset</text>
      <text class="pillar-label" x="84" y="30" text-anchor="middle" dominant-baseline="middle">Workout</text>
      <text class="pillar-label" x="0" y="90" text-anchor="middle" dominant-baseline="middle">Diet</text>
      <text class="pillar-label" x="-84" y="30" text-anchor="middle" dominant-baseline="middle">Recover</text>
    </g>

    <!-- program names -->
    <text class="program-name"><textPath href="#calm-grid-arc" startOffset="50%" text-anchor="middle">The Calm Grid</textPath></text>
    <text class="program-name"><textPath href="#foreguard-arc" startOffset="50%" text-anchor="middle">Foreguard</textPath></text>
    <text class="program-name"><textPath href="#stride-arc" startOffset="50%" text-anchor="middle">Stride Onward</textPath></text>
  </svg>
</main>
</body>
</html>
```